we need a design for Water Bottle Lable Wrap
The product is called Corvane Water is a restructured water. its a very healthy and rejuvenating water
we were looking at using as a tag ling Restore, Recover, Rejuvenate.

```html
<!DOCTYPE html>
<html lang="en">
<head>
<meta charset="utf-8">
<title>Corvane Water – Label Wrap</title>
<link rel="stylesheet" href="https://fonts.googleapis.com/css2?family=Montserrat:wght@300;400;600;700;800&display=swap">
<style>
  :root {
    --navy: #00324f;
    --sky-light: #7dd8f1;
    --sky-mid: #00b8e6;
    --line-cyan: #00b5e2;
    --brand-blue: #005a96;
    --ink-blue: #0b4f8a;
    --white: #ffffff;
  }
  html, body {
    margin: 0;
    padding: 0;
    width: 1200px;
    height: 989px;
    overflow: hidden;
    background: var(--white);
  }
  .label-wrap {
    position: relative;
    width: 1200px;
    height: 989px;
    overflow: hidden;
  }
  .label-art {
    display: block;
    width: 1200px;
    height: 989px;
  }
  .field-navy { fill: var(--navy); }
  .field-light { fill: var(--sky-light); }
  .field-mid { fill: var(--sky-mid); }
  .edge-line { stroke: var(--line-cyan); stroke-width: 2; fill: none; }
  .brand-dot { fill: var(--brand-blue); }
  .brand-name {
    font-family: "Montserrat", sans-serif;
    font-weight: 800;
    font-size: 108px;
    fill: var(--white);
  }
  .brand-sub {
    font-family: "Montserrat", sans-serif;
    font-weight: 300;
    font-size: 37px;
    fill: var(--ink-blue);
  }
  .tagline {
    font-family: "Montserrat", sans-serif;
    font-weight: 400;
    font-size: 29px;
    fill: var(--ink-blue);
  }
  .tagline .strong { font-weight: 700; }
</style>
</head>
<body>
<main class="label-wrap">
  <svg class="label-art" viewBox="0 0 1200 989" xmlns="http://www.w3.org/2000/svg">
    <polygon class="field-mid" points="0,507 330,837 178,989 0,989"/>
    <polygon class="field-light" points="299,0 442,0 806,361 330,837 0,507 0,307"/>
    <polygon class="field-navy" points="0,0 299,0 0,307"/>
    <polyline class="edge-line" points="1170,0 806,361 178,989"/>

    <circle class="brand-dot" cx="370" cy="233" r="98"/>

    <text class="brand-name" x="370" y="430" text-anchor="middle" textLength="496" lengthAdjust="spacingAndGlyphs">CORVANE</text>
    <text class="brand-sub" x="372" y="472" text-anchor="middle" textLength="319" lengthAdjust="spacing">WATER</text>
    <text class="tagline" x="373" y="514" text-anchor="middle" textLength="481" lengthAdjust="spacingAndGlyphs"><tspan class="strong">100%</tspan> Pure <tspan class="strong">Restructured</tspan> Water</text>
  </svg>
</main>
</body>
</html>
```